Website design for an Italian restaurant in Amsterdam

I need a design for a client of mine. It is for Teatro Lunaverde, an Italian restaurant in Amsterdam.
We are going for a clean, modern look but we also need to realise an authentic feel.
The restaurant is located in an old movie theatre, that is where the name Teatro Lunaverde comes from.
Industry/Entity Type
Italian Restaurant
Number of Pages Required
1 page
Font styles to use
Sans Serif
Colors
Designer to choose colors to be used in the design.

```html
<!DOCTYPE html>
<html lang="en">
<head>
<meta charset="utf-8">
<title>Teatro Lunaverde – Italian restaurant in Amsterdam</title>
<link rel="stylesheet" href="https://fonts.googleapis.com/css2?family=Raleway:wght@500;600;700;800&family=Open+Sans:wght@400;600;700&display=swap">
<style>
:root{
  --wine:#a44a5c;
  --wine-dark:#8e3b4c;
  --ink:#1f1f1f;
  --text:#555555;
  --paper:#ffffff;
  --mist:#f2f2f2;
  --line:#dedede;
  --night:#171313;
}
*{box-sizing:border-box;margin:0;padding:0}
html,body{width:1200px;height:3066px;overflow:hidden}
body{font-family:"Open Sans",Arial,sans-serif;color:var(--text);background:var(--paper);position:relative}
.abs{position:absolute}
section,header,footer{position:relative;width:1200px}
.btn{position:absolute;display:flex;align-items:center;justify-content:center;border-radius:30px;font-family:"Open Sans",Arial,sans-serif;font-weight:700;font-size:14px;letter-spacing:.5px;text-transform:uppercase;white-space:nowrap}
.btn-solid{background:var(--wine);color:#fff}
.btn-outline{border:2px solid #fff;color:#fff}

/* hero */
.hero{height:644px;background:radial-gradient(ellipse at 60% 45%,#6b4a30 0%,#3a2619 40%,#140d0a 100%)}
.hero-photo{position:absolute;inset:0;background:linear-gradient(180deg,rgba(40,25,15,.2),rgba(0,0,0,.35)),radial-gradient(circle at 30% 70%,rgba(230,200,160,.35),transparent 35%),radial-gradient(circle at 75% 30%,rgba(200,170,150,.35),transparent 30%)}
.topbar{position:absolute;left:0;top:38px;width:1200px;height:85px;background:rgba(15,12,12,.82)}
.brand{position:absolute;left:98px;top:22px;display:flex;align-items:center;gap:12px;color:#fff}
.brand-dot{width:30px;height:30px;border-radius:50%;background:var(--wine)}
.brand-name{font-family:"Raleway",Arial,sans-serif;font-weight:600;font-size:21px;letter-spacing:1px;text-transform:uppercase;line-height:1}
.brand-tag{display:block;font-size:9px;letter-spacing:1px;color:var(--wine);margin-top:3px;text-transform:none}
.nav{position:absolute;top:0;height:85px;display:flex;align-items:center;font-family:"Raleway",Arial,sans-serif;font-weight:700;font-size:15px;color:#fff;text-transform:uppercase}
.nav.active{color:var(--wine)}
.hero-title{position:absolute;left:0;width:1200px;top:238px;text-align:center;font-family:"Raleway",Arial,sans-serif;font-weight:800;font-size:76px;color:#fff;letter-spacing:1px}
.hero-sub{position:absolute;left:0;width:1200px;top:336px;text-align:center;font-size:23px;color:#fff}
.dots{position:absolute;top:576px;left:566px;display:flex;gap:4px}
.dots span{width:13px;height:13px;border-radius:50%;border:2px solid #fff}
.dots span.on{background:#fff}

.notice{height:73px;background:var(--wine);display:flex;align-items:center;justify-content:center;font-family:"Raleway",Arial,sans-serif;font-weight:700;font-size:32px;color:#fff}

/* story */
.story{height:575px}
.kicker{font-family:"Raleway",Arial,sans-serif;font-weight:700;font-size:20px;color:var(--ink)}
.h2{font-family:"Raleway",Arial,sans-serif;font-weight:700;color:var(--ink);text-transform:uppercase}
.copy{font-size:14px;line-height:28px;color:var(--text)}
.photo{position:absolute}

/* about */
.about{height:527px;background:var(--mist)}
.about-card{position:absolute;left:98px;top:63px;width:1004px;height:399px;background:#fff;box-shadow:0 1px 4px rgba(0,0,0,.18)}

/* menu */
.menu{height:450px}
.menu-card{position:absolute;top:178px;width:481px;height:180px;background:#fff;box-shadow:0 1px 5px rgba(0,0,0,.2)}
.menu-card .photo{left:0;top:0;width:188px;height:180px}
.menu-card h3{position:absolute;left:222px;top:28px;font-family:"Raleway",Arial,sans-serif;font-weight:700;font-size:18px;color:var(--ink);text-transform:uppercase}
.ticks{position:absolute;left:222px;top:62px;list-style:none;font-size:14px;line-height:26px;color:var(--text)}
.ticks li{display:flex;align-items:center;gap:10px}

/* features */
.features{height:212px;background:var(--wine)}
.feature{position:absolute;top:0;height:212px;color:#fff}
.feature-icon{position:absolute;left:0;top:21px;width:86px;height:86px;border-radius:50%;background:#fff;display:flex;align-items:center;justify-content:center}
.feature h3{position:absolute;left:110px;top:26px;font-family:"Raleway",Arial,sans-serif;font-weight:700;font-size:25px}
.feature p{position:absolute;left:110px;top:64px;width:212px;font-size:14px;line-height:24px}
.divider{position:absolute;top:38px;width:1px;height:136px;background:rgba(255,255,255,.35)}

/* contact */
.contact{height:585px;background:radial-gradient(ellipse at 30% 40%,#3b2a20 0%,#1c1512 55%,#0e0b0a 100%);color:#fff}
.contact-title{position:absolute;left:0;width:1200px;top:70px;text-align:center;font-family:"Raleway",Arial,sans-serif;font-weight:700;font-size:36px}
.label{position:absolute;font-size:11px;font-weight:400;text-transform:uppercase;letter-spacing:.5px}
.col-head{position:absolute;font-size:15px;font-weight:700;text-transform:uppercase}
.field{position:absolute;background:#fff;border:1px solid #ccc}
.info-icon{position:absolute;left:811px;width:34px;height:34px;border-radius:50%;background:#fff;display:flex;align-items:center;justify-content:center}
.info-text{position:absolute;left:863px;font-size:12px;line-height:20px}
.hours{position:absolute;left:809px;font-size:12px}
.hours-time{position:absolute;left:1008px;font-size:12px}
.rule{position:absolute;left:98px;top:499px;width:1004px;height:1px;background:rgba(255,255,255,.25)}
.copyright{position:absolute;left:98px;top:528px;font-size:12px}
.social{position:absolute;top:524px;width:26px;height:26px;background:#fff;border-radius:3px}
</style>
</head>
<body>

<header class="hero">
  <div class="hero-photo" role="img" aria-label="Photo of the candle-lit restaurant hall in the old theatre, with set tables and a projection screen"></div>
  <div class="topbar">
    <div class="brand">
      <span class="brand-dot"></span>
      <span class="brand-name">Teatro Lunaverde<span class="brand-tag">Ristorante Italiano</span></span>
    </div>
    <span class="nav active" style="left:499px">Home</span>
    <span class="nav" style="left:576px">Menu (New)</span>
    <span class="nav" style="left:707px">Groupmenu</span>
    <span class="nav" style="left:840px">Reservation</span>
    <span class="nav" style="left:979px">Contact</span>
    <svg class="abs" style="left:1086px;top:33px" width="18" height="18" viewBox="0 0 18 18"><circle cx="7.5" cy="7.5" r="5.5" fill="none" stroke="#fff" stroke-width="2.4"/><line x1="11.5" y1="11.5" x2="16.5" y2="16.5" stroke="#fff" stroke-width="2.6" stroke-linecap="round"/></svg>
  </div>
  <h1 class="hero-title">TEATRO LUNAVERDE</h1>
  <p class="hero-sub">We are an Italian restaurant from Amsterdam</p>
  <span class="btn btn-outline" style="left:497px;top:399px;width:204px;height:56px;font-size:16px">Reserve a table</span>
  <div class="dots"><span class="on"></span><span></span><span></span><span></span></div>
</header>

<div class="notice">NOW OPEN ON SUNDAYS !</div>

<section class="story">
  <p class="kicker abs" style="left:0;width:624px;top:132px;text-align:center">Italian restaurant</p>
  <h2 class="h2 abs" style="left:0;width:624px;top:166px;text-align:center;font-size:38px">Our Story</h2>
  <p class="copy abs" style="left:107px;width:410px;top:230px;text-align:center;font-size:13px">At vero eos et accusamus et iusto odio dignissimos ducimus qui blan ditiis praesentium voluptatum deleniti atque corrupti qu os dolores et quas molestias excepturi sint occaecati cupiditate non provid lpa qui officia deserunt mollitia ani</p>
  <span class="btn btn-solid" style="left:237px;top:379px;width:151px;height:51px">Read more</span>
  <div class="photo" style="left:605px;top:84px;width:159px;height:397px;background:linear-gradient(180deg,#2a1d1a 0%,#5a2a1c 45%,#b0552f 65%,#6e7a3a 85%,#3a2a20 100%)" role="img" aria-label="Photo of a lobster pasta dish"></div>
  <div class="photo" style="left:773px;top:84px;width:159px;height:397px;background:linear-gradient(180deg,#4a3b35 0%,#1a1414 30%,#120e0e 70%,#3c3030 100%)" role="img" aria-label="Photo of a bottle of Italian red wine"></div>
  <div class="photo" style="left:940px;top:84px;width:160px;height:397px;background:linear-gradient(180deg,#2a2220 0%,#4a5a2a 30%,#c2452e 55%,#e8e0d8 85%,#b8aca4 100%)" role="img" aria-label="Photo of bruschetta with tomato and basil"></div>
</section>

<section class="about">
  <div class="about-card">
    <div class="photo" style="left:4px;top:4px;width:419px;height:391px;background:radial-gradient(ellipse at 45% 45%,#8a6a3a 0%,#a89a6a 35%,#d8d4c6 65%,#a8a49a 100%)" role="img" aria-label="Photo of a plated risotto with green asparagus"></div>
    <h2 class="h2 abs" style="left:460px;top:40px;font-size:36px">About Teatro Lunaverde</h2>
    <p class="copy abs" style="left:460px;top:106px;width:510px;font-size:12.5px;line-height:26px">At vero eos et accusamus et iusto odio dignissimos ducimus qui blanditiis praesetium voluptatum deleniti atque corrupti quos dolor.</p>
    <p class="copy abs" style="left:460px;top:180px;width:510px;font-size:12.5px;line-height:26px">Quas molestias excepturi sint occaecati cupiditate non provident, similique sunt incul pa qui officia deserunt mollitia animi, id est laborum et dolorum fuga. Et harum qjem rerum facilis est et expedita distinctio. Nam libero tempore, cum soluta nobis est elig endi optio cumque nihil impedit quo minus id quod.</p>
    <span class="btn btn-solid" style="left:460px;top:303px;width:153px;height:49px">Read more</span>
  </div>
</section>

<section class="menu">
  <h2 class="h2 abs" style="left:0;width:1200px;top:92px;text-align:center;font-size:36px">Menu</h2>
  <div class="menu-card" style="left:98px">
    <div class="photo" style="background:linear-gradient(160deg,#6a2a1a 0%,#c2452e 45%,#e6c8a0 80%,#f2ece4 100%)" role="img" aria-label="Photo of bruschetta and a tomato salad"></div>
    <h3>Menu (New)</h3>
    <ul class="ticks">
      <li><svg width="12" height="10" viewBox="0 0 12 10"><path d="M1 5l3.5 3.5L11 1.5" fill="none" stroke="var(--wine)" stroke-width="2.4"/></svg>Antipasti</li>
      <li><svg width="12" height="10" viewBox="0 0 12 10"><path d="M1 5l3.5 3.5L11 1.5" fill="none" stroke="var(--wine)" stroke-width="2.4"/></svg>Le Insalate</li>
      <li><svg width="12" height="10" viewBox="0 0 12 10"><path d="M1 5l3.5 3.5L11 1.5" fill="none" stroke="var(--wine)" stroke-width="2.4"/></svg>Le Paste</li>
      <li><svg width="12" height="10" viewBox="0 0 12 10"><path d="M1 5l3.5 3.5L11 1.5" fill="none" stroke="var(--wine)" stroke-width="2.4"/></svg>Il Pesce</li>
    </ul>
  </div>
  <div class="menu-card" style="left:619px">
    <div class="photo" style="background:linear-gradient(160deg,#3a2a1a 0%,#6a8a2a 35%,#c8362a 60%,#f4f0e8 100%)" role="img" aria-label="Photo of a caprese salad with mozzarella and tomato"></div>
    <h3>Group Menu</h3>
    <ul class="ticks">
      <li><svg width="12" height="10" viewBox="0 0 12 10"><path d="M1 5l3.5 3.5L11 1.5" fill="none" stroke="var(--wine)" stroke-width="2.4"/></svg>Antipasti</li>
      <li><svg width="12" height="10" viewBox="0 0 12 10"><path d="M1 5l3.5 3.5L11 1.5" fill="none" stroke="var(--wine)" stroke-width="2.4"/></svg>Secondi</li>
      <li><svg width="12" height="10" viewBox="0 0 12 10"><path d="M1 5l3.5 3.5L11 1.5" fill="none" stroke="var(--wine)" stroke-width="2.4"/></svg>Dolci</li>
      <li><svg width="12" height="10" viewBox="0 0 12 10"><path d="M1 5l3.5 3.5L11 1.5" fill="none" stroke="var(--wine)" stroke-width="2.4"/></svg>Il Pesce</li>
    </ul>
  </div>
</section>

<section class="features">
  <div class="feature" style="left:100px;width:330px">
    <div class="feature-icon"><svg width="40" height="40" viewBox="0 0 40 40"><rect x="4" y="7" width="32" height="29" rx="3" fill="none" stroke="var(--wine)" stroke-width="3"/><rect x="4" y="7" width="32" height="8" fill="var(--wine)"/><line x1="12" y1="3" x2="12" y2="10" stroke="var(--wine)" stroke-width="3"/><line x1="28" y1="3" x2="28" y2="10" stroke="var(--wine)" stroke-width="3"/><g fill="var(--wine)"><rect x="9" y="19" width="5" height="4"/><rect x="17.5" y="19" width="5" height="4"/><rect x="26" y="19" width="5" height="4"/><rect x="9" y="27" width="5" height="4"/><rect x="17.5" y="27" width="5" height="4"/><rect x="26" y="27" width="5" height="4"/></g></svg></div>
    <h3>RESERVATION</h3>
    <p>Tables can be reserved online through our website</p>
    <span class="btn btn-outline" style="left:110px;top:125px;width:158px;height:42px;font-size:13px">Reserve a table</span>
  </div>
  <div class="divider" style="left:438px"></div>
  <div class="feature" style="left:461px;width:330px">
    <div class="feature-icon"><svg width="40" height="36" viewBox="0 0 40 36"><rect x="3" y="4" width="34" height="28" fill="none" stroke="var(--wine)" stroke-width="3"/><circle cx="13" cy="13" r="3.5" fill="var(--wine)"/><path d="M6 29l10-10 6 6 5-5 8 9z" fill="var(--wine)"/></svg></div>
    <h3>Portfolio</h3>
    <p>Tables can be reserved online through our website</p>
    <span class="btn btn-outline" style="left:110px;top:125px;width:158px;height:42px;font-size:13px">View gallery</span>
  </div>
  <div class="divider" style="left:804px"></div>
  <div class="feature" style="left:832px;width:330px">
    <div class="feature-icon"><svg width="42" height="38" viewBox="0 0 42 38"><ellipse cx="17" cy="14" rx="14" ry="10" fill="var(--wine)"/><path d="M8 21l-3 8 9-5z" fill="var(--wine)"/><ellipse cx="28" cy="22" rx="11" ry="8" fill="none" stroke="var(--wine)" stroke-width="3"/><path d="M34 28l3 6-8-4z" fill="var(--wine)"/></svg></div>
    <h3>Blog</h3>
    <p>Tables can be reserved online through our website</p>
    <span class="btn btn-outline" style="left:110px;top:125px;width:158px;height:42px;font-size:13px">View blog</span>
  </div>
</section>

<footer class="contact">
  <div class="abs" style="inset:0;background:radial-gradient(circle at 70% 60%,rgba(120,80,50,.25),transparent 40%)" role="img" aria-label="Dark, blurred background photo of food on a table"></div>
  <h2 class="contact-title">CONTACT US</h2>

  <span class="col-head" style="left:98px;top:130px">Contact form</span>
  <span class="label" style="left:98px;top:174px">Name :</span>
  <span class="label" style="left:417px;top:174px">Phone no :</span>
  <div class="field" style="left:98px;top:203px;width:313px;height:33px"></div>
  <div class="field" style="left:417px;top:203px;width:313px;height:33px"></div>
  <span class="label" style="left:98px;top:244px">Email :</span>
  <div class="field" style="left:98px;top:268px;width:632px;height:33px"></div>
  <span class="label" style="left:98px;top:311px">Message :</span>
  <div class="field" style="left:98px;top:336px;width:632px;height:82px"></div>
  <span class="btn btn-solid" style="left:630px;top:426px;width:100px;height:34px;font-size:13px">Submit</span>

  <span class="col-head" style="left:809px;top:130px">Contact information</span>
  <div class="info-icon" style="top:176px"><svg width="14" height="18" viewBox="0 0 14 18"><path d="M7 1a6 6 0 0 0-6 6c0 4.5 6 10 6 10s6-5.5 6-10a6 6 0 0 0-6-6z" fill="#1c1512"/><circle cx="7" cy="7" r="2.2" fill="#fff"/></svg></div>
  <p class="info-text" style="top:172px">Lindengracht 74<br>1015 KK Amsterdam</p>
  <div class="info-icon" style="top:235px"><svg width="16" height="12" viewBox="0 0 16 12"><rect x="0" y="0" width="16" height="12" rx="1.5" fill="#1c1512"/><path d="M1 1.5l7 5 7-5" fill="none" stroke="#fff" stroke-width="1.4"/></svg></div>
  <p class="info-text" style="top:242px">info@teatrolunaverde.info</p>
  <div class="info-icon" style="top:290px"><svg width="16" height="16" viewBox="0 0 16 16"><path d="M3.5 1l3 3-1.8 2a9 9 0 0 0 5.3 5.3l2-1.8 3 3-2 2.5C7 14.5 1.5 9 1 3z" fill="#1c1512"/></svg></div>
  <p class="info-text" style="top:298px">+31 20 555 0192</p>

  <span class="col-head" style="left:809px;top:359px">Opening hours</span>
  <span class="hours" style="top:391px">Monday -</span><span class="hours-time" style="top:391px">Closed</span>
  <span class="hours" style="top:416px">Tuesday, Thursday</span><span class="hours-time" style="top:416px">18:00 - 23:00</span>
  <span class="hours" style="top:442px">Sunday</span><span class="hours-time" style="top:442px">Closed</span>

  <div class="rule"></div>
  <p class="copyright">Copyrights © 2018, Teatro Lunaverde . All Rights Reserved.</p>
  <span class="social" style="left:955px"></span>
  <span class="social" style="left:995px"></span>
  <span class="social" style="left:1035px"></span>
  <span class="social" style="left:1075px"></span>
</footer>

</body>
</html>
```